Brenvik Innovations
Professional
Daniel Marlow
CEO
5812-4 Calloway Ave #2267
Houston, TX 77194
Daniel@BrenvikInnovations.com
BrenvikInnovations.com
Feel free to play with the function of the business card if possible as seen in: http://www.trelvaform-studio.com/blog/wp-content/uploads/2009/12/lock-picking-business-card.jpg. Card can be paper plastic or metal.
Our company specializes in artificial intelligence, Unmanned aerial vehicles human-machine interfaces and lasers. Please keep this in mind in your designs.
surprise me, I will refine my requirement here after I see a few submissions.
Here are the business logo files

```html
<!DOCTYPE html>
<html lang="en">
<head>
<meta charset="utf-8">
<title>Brenvik Innovations – Business Card</title>
<link rel="stylesheet" href="https://fonts.googleapis.com/css2?family=Arimo:wght@400;700&display=swap">
<style>
  :root {
    --backdrop: #e4e2de;
    --card: #ffffff;
    --brand-navy: #34317a;
    --text-grey: #9a9a9a;
    --text-dark-grey: #8a8a8a;
  }
  html, body {
    margin: 0;
    padding: 0;
    width: 1200px;
    height: 1039px;
    overflow: hidden;
    background: var(--backdrop);
    font-family: "Arimo", Arial, sans-serif;
  }
  .canvas {
    position: relative;
    width: 1200px;
    height: 1039px;
  }
  .card-shapes {
    position: absolute;
    inset: 0;
  }
  .card-shape {
    fill: var(--card);
  }
  .brand {
    position: absolute;
    display: flex;
    align-items: center;
    gap: 14px;
    color: var(--brand-navy);
    font-weight: 700;
  }
  .brand-mark {
    width: 44px;
    height: 44px;
    background: var(--brand-navy);
    flex: none;
  }
  .brand-name {
    display: flex;
    flex-direction: column;
    line-height: 1;
  }
  .brand-name .primary { font-size: 44px; letter-spacing: 1px; }
  .brand-name .secondary { font-size: 17px; letter-spacing: 6.5px; margin-top: 4px; }

  .brand--front { left: 118px; top: 146px; }
  .brand--back  { left: 628px; top: 604px; }

  .contact {
    position: absolute;
    left: 213px;
    top: 246px;
    color: var(--text-grey);
  }
  .contact .person-name {
    font-size: 22px;
    font-weight: 700;
    color: var(--text-dark-grey);
    margin: 0;
  }
  .contact .person-title {
    font-size: 21px;
    margin: 2px 0 38px;
  }
  .contact .details {
    font-size: 18px;
    line-height: 24px;
    margin: 0;
  }
  .contact .label { font-weight: 700; color: var(--brand-navy); }

  .website {
    position: absolute;
    left: 722px;
    top: 829px;
    font-size: 17px;
    color: var(--brand-navy);
  }
</style>
</head>
<body>
<main class="canvas">
  <svg class="card-shapes" width="1200" height="1039" viewBox="0 0 1200 1039" aria-hidden="true">
    <!-- front card with key-style notch on the right -->
    <path class="card-shape" d="M85 107 H655 L595 215 L760 262 L605 330 L540 465 H85 Z"/>
    <!-- back card with matching notch on the left -->
    <path class="card-shape" d="M455 507 H1022 V862 H605 L510 770 L403 695 L505 612 Z"/>
  </svg>

  <section class="card-front">
    <div class="brand brand--front">
      <span class="brand-mark"></span>
      <span class="brand-name"><span class="primary">BRENVIK</span><span class="secondary">INNOVATIONS</span></span>
    </div>
    <div class="contact">
      <p class="person-name">Daniel Marlow</p>
      <p class="person-title">CEO</p>
      <p class="details">
        5812-4 Calloway Ave #2267<br>
        Houston, TX 77194<br>
        <span class="label">C</span> : 214-555-0187<br>
        <span class="label">E</span> : Daniel@BrenvikInnovations.com
      </p>
    </div>
  </section>

  <section class="card-back">
    <div class="brand brand--back">
      <span class="brand-mark"></span>
      <span class="brand-name"><span class="primary">BRENVIK</span><span class="secondary">INNOVATIONS</span></span>
    </div>
    <p class="website" style="margin:0">www.BrenvikInnovations.com</p>
  </section>
</main>
</body>
</html>
```